Kit Layout de Posts para Redes Sociais (Facebook, Instagram e etc)para Dra Marcela Toledano
Postado por: marcelatoledano_5830174416   Estou Offline
Projeto para criar:
Kit Layout de Posts para Redes Sociais (Facebook, Instagram e etc)
Clientes com PC preferem arquivos em CorelDraw (CDR).
Imagem: Imagem JPG (alta resoluçao) PNG em camadas PSD em camadas PDF Sem Preferência Tipos possíveis: Imagem JPG (alta resoluçao), PNG em camadas, PSD em camadas, PDF.

```html
<!DOCTYPE html>
<html lang="pt-BR">
<head>
<meta charset="utf-8">
<title>Post – Dra. Marcela Toledano</title>
<link href="https://fonts.googleapis.com/css2?family=Montserrat:wght@300;400&display=swap" rel="stylesheet">
<style>
  :root{
    --plum:#6e4a62;
    --band:#7a4e69;
    --gold:#c9a25f;
    --white:#ffffff;
    --paper:#fdfcfc;
  }
  html,body{margin:0;padding:0;overflow:hidden;background:var(--paper);}
  .post{
    position:relative;width:1200px;height:1200px;overflow:hidden;
    background:var(--paper);
    font-family:"Montserrat",sans-serif;
  }
  .portrait-area{
    position:absolute;left:540px;top:0;width:660px;height:980px;
    background:
      linear-gradient(90deg,var(--paper) 0%,rgba(253,252,252,0) 22%),
      radial-gradient(ellipse 55% 60% at 62% 42%,#e9c9b6 0%,#dcb6a0 45%,#efe4df 80%,#f7f3f2 100%);
  }
  .headline{
    position:absolute;left:66px;top:160px;margin:0;
    color:var(--plum);font-weight:400;line-height:1;
  }
  .headline .line-1{display:block;font-size:98px;letter-spacing:2px;}
  .headline .line-2{display:block;font-size:176px;letter-spacing:6px;margin-top:2px;}
  .accent-bar{
    position:absolute;left:30px;top:178px;width:8px;height:190px;
    background:linear-gradient(180deg,#e2c489,var(--gold) 60%,#a57d3e);
  }
  .footer-band{position:absolute;left:0;top:0;width:1200px;height:1200px;}
  .brand{
    position:absolute;left:90px;top:1010px;display:flex;align-items:center;gap:26px;
    color:var(--white);font-weight:300;
  }
  .brand-mark{
    width:96px;height:96px;border:3px solid var(--gold);border-radius:50%;box-sizing:border-box;
  }
  .brand-name{font-size:40px;line-height:1.12;letter-spacing:1px;}
  .brand-name small{display:block;font-size:26px;}
  .divider{
    position:absolute;left:628px;top:1060px;width:2px;height:110px;background:rgba(255,255,255,.45);
  }
  .contacts{
    position:absolute;left:772px;top:1068px;margin:0;padding:0;list-style:none;
    color:var(--white);font-size:29px;font-weight:400;
  }
  .contacts li{display:flex;align-items:center;gap:16px;height:50px;}
  .contact-icon{
    width:32px;height:32px;border-radius:50%;background:var(--gold);
    display:flex;align-items:center;justify-content:center;flex:none;
  }
</style>
</head>
<body>
  <main class="post">
    <div class="portrait-area" role="img" aria-label="Fotografia de mulher com maquiagem suave recebendo avaliação facial por mãos com luvas brancas"></div>

    <span class="accent-bar"></span>
    <h1 class="headline"><span class="line-1">SEU TEXTO</span><span class="line-2">AQUI</span></h1>

    <svg class="footer-band" viewBox="0 0 1200 1200" aria-hidden="true">
      <defs>
        <linearGradient id="goldLine" x1="0" x2="1">
          <stop offset="0" stop-color="#b08a4a"/>
          <stop offset=".5" stop-color="#e6c98f"/>
          <stop offset="1" stop-color="#b08a4a"/>
        </linearGradient>
      </defs>
      <path d="M0 872 C380 900 760 960 1200 930 L1200 1200 L0 1200 Z" fill="var(--band)"/>
      <path d="M250 930 C600 965 900 960 1200 940" fill="none" stroke="url(#goldLine)" stroke-width="6"/>
    </svg>

    <div class="brand">
      <span class="brand-mark"></span>
      <div class="brand-name"><small>Dra.</small>Marcela<br>Toledano</div>
    </div>

    <span class="divider"></span>

    <ul class="contacts">
      <li>
        <span class="contact-icon">
          <svg width="18" height="18" viewBox="0 0 24 24"><path fill="#fff" d="M6.6 10.8a15.1 15.1 0 0 0 6.6 6.6l2.2-2.2c.3-.3.7-.4 1-.2 1.1.4 2.3.6 3.6.6.6 0 1 .4 1 1V20c0 .6-.4 1-1 1A17 17 0 0 1 3 4c0-.6.4-1 1-1h3.5c.6 0 1 .4 1 1 0 1.3.2 2.5.6 3.6.1.3 0 .7-.2 1z"/></svg>
        </span>
        (00) 2222-2222
      </li>
      <li>
        <span class="contact-icon"></span>
        @DraMarcelaToledano
      </li>
    </ul>
  </main>
</body>
</html>
```